Lantern Marketing Group (LMG)

This is for my business cards. I want a Nice anfd Elegant Business Card to be Designed, Using more or less of the same colors of my logo that i have attached.i would like to have these business cards forever

Thank you

Thank you

Thank you

Contact Information for Business Card

Calvin Ortega
Lantern Marketing Group
C.(555) 482-1306
E-Mail. COrtega@lanternmgroup.example

Font styles to use
Serif
Sans Serif

Colors
d0dfed
cbcbcb
cee9f5

Requirements
Must have
• (LMG)
• Lantern Marketing Group
Nice to have
• 3D affects
Should not have
• Please try not using the flat version of the logo try and use the 3d version please

```html
<!DOCTYPE html>
<html lang="en">
<head>
<meta charset="utf-8">
<title>Lantern Marketing Group – Business Cards</title>
<link rel="stylesheet" href="https://fonts.googleapis.com/css2?family=Open+Sans:wght@400;600;700&family=PT+Sans+Narrow:wght@700&display=swap">
<style>
  :root {
    --stage: #070707;
    --ice: #d2f6f8;
    --ice-light: #f2feff;
    --stone: #ced5d3;
    --stone-light: #eef0ef;
    --paper: #ffffff;
    --ink: #5b6468;
    --mark: #97a3a4;
    --mark-dark: #8e9a9b;
    --icon: #3a3f42;
    --edge: #bfc5c5;
  }
  * { box-sizing: border-box; margin: 0; padding: 0; }
  html, body { width: 1200px; height: 1000px; overflow: hidden; background: var(--stage); }
  .sheet { position: relative; width: 1200px; height: 1000px; }
  .card {
    position: absolute; width: 524px; height: 322px; overflow: hidden;
    border: 1px solid var(--edge);
  }
  .card svg.bg { position: absolute; inset: 0; }
  .front-ice { left: 68px; top: 166px; }
  .front-stone { left: 608px; top: 166px; }
  .back-stone { left: 68px; top: 504px; background: var(--paper); }
  .back-ice { left: 608px; top: 504px; background: var(--paper); }

  .brand {
    position: absolute; left: 102px; top: 122px;
    font-family: "PT Sans Narrow", "Arial Narrow", sans-serif; font-weight: 700;
    color: var(--mark); line-height: 1;
  }
  .brand .word { display: block; font-size: 48px; letter-spacing: 0.5px; }
  .brand .sub { display: block; font-size: 26px; margin-top: 2px; }
  .brand-square {
    position: absolute; left: 290px; top: 82px; width: 128px; height: 128px;
    background: var(--mark);
  }
  .front-stone .brand, .front-stone .brand-square { color: var(--mark-dark); }
  .front-stone .brand-square { background: var(--mark-dark); }

  .initials {
    position: absolute; right: 56px; top: 80px;
    font-family: "PT Sans Narrow", "Arial Narrow", sans-serif; font-weight: 700;
    font-size: 58px; line-height: 1;
  }
  .back-stone .initials { color: var(--ice); }
  .back-ice .initials { color: var(--mark); }

  .holder { position: absolute; left: 53px; top: 92px; font-family: "Open Sans", sans-serif; color: var(--ink); }
  .holder .name { font-size: 18px; font-weight: 700; letter-spacing: 0.2px; }
  .holder .company { font-size: 15px; font-weight: 400; margin-top: 4px; }
  .contacts { position: absolute; left: 52px; top: 178px; list-style: none; font-family: "Open Sans", sans-serif; font-size: 15.5px; color: var(--ink); }
  .contacts li { display: flex; align-items: center; height: 26px; margin-bottom: 12px; }
  .contacts svg { width: 26px; height: 26px; margin-right: 8px; flex: none; }
</style>
</head>
<body>
<main class="sheet">

  <section class="card front-ice">
    <svg class="bg" width="524" height="322" viewBox="0 0 524 322">
      <defs>
        <radialGradient id="iceGlow" cx="0.55" cy="0.35" r="0.6">
          <stop offset="0" stop-color="var(--ice-light)"/>
          <stop offset="1" stop-color="var(--ice)"/>
        </radialGradient>
      </defs>
      <rect width="524" height="322" fill="url(#iceGlow)"/>
      <polygon points="92,322 524,66 524,322" fill="#ffffff" opacity="0.55"/>
    </svg>
    <div class="brand"><span class="word">LANTERN</span><span class="sub">Marketing Group</span></div>
    <div class="brand-square"></div>
  </section>

  <section class="card front-stone">
    <svg class="bg" width="524" height="322" viewBox="0 0 524 322">
      <defs>
        <radialGradient id="stoneGlow" cx="0.7" cy="0.2" r="0.6">
          <stop offset="0" stop-color="var(--stone-light)"/>
          <stop offset="1" stop-color="var(--stone)"/>
        </radialGradient>
      </defs>
      <rect width="524" height="322" fill="url(#stoneGlow)"/>
      <polygon points="170,322 524,66 524,322" fill="#ffffff" opacity="0.25"/>
    </svg>
    <div class="brand"><span class="word">LANTERN</span><span class="sub">Marketing Group</span></div>
    <div class="brand-square"></div>
  </section>

  <section class="card back-stone">
    <svg class="bg" width="524" height="322" viewBox="0 0 524 322">
      <polygon points="144,0 524,0 524,262" fill="var(--stone)"/>
    </svg>
    <div class="initials">LMG</div>
    <div class="holder"><p class="name">CALVIN ORTEGA</p><p class="company">Lantern Marketing Group C.</p></div>
    <ul class="contacts">
      <li><svg viewBox="0 0 26 26"><circle cx="13" cy="13" r="13" fill="var(--icon)"/><path d="M9.5 7.5l2 2.6-1.2 1.3c.7 1.6 1.9 2.8 3.4 3.5l1.3-1.2 2.6 2-1.1 1.8c-4.3-.4-8.2-4.3-8.6-8.6z" fill="#fff"/></svg>(555) 482-1306</li>
      <li><svg viewBox="0 0 26 26"><circle cx="13" cy="13" r="13" fill="var(--icon)"/><rect x="7.5" y="9" width="11" height="8" fill="#fff"/><path d="M7.5 9l5.5 4.5 5.5-4.5" fill="none" stroke="var(--icon)" stroke-width="1"/></svg>COrtega@lanternmgroup.example</li>
    </ul>
  </section>

  <section class="card back-ice">
    <svg class="bg" width="524" height="322" viewBox="0 0 524 322">
      <polygon points="144,0 524,0 524,262" fill="var(--ice)"/>
    </svg>
    <div class="initials">LMG</div>
    <div class="holder"><p class="name">CALVIN ORTEGA</p><p class="company">Lantern Marketing Group C.</p></div>
    <ul class="contacts">
      <li><svg viewBox="0 0 26 26"><circle cx="13" cy="13" r="13" fill="var(--icon)"/><path d="M9.5 7.5l2 2.6-1.2 1.3c.7 1.6 1.9 2.8 3.4 3.5l1.3-1.2 2.6 2-1.1 1.8c-4.3-.4-8.2-4.3-8.6-8.6z" fill="#fff"/></svg>(555) 482-1306</li>
      <li><svg viewBox="0 0 26 26"><circle cx="13" cy="13" r="13" fill="var(--icon)"/><rect x="7.5" y="9" width="11" height="8" fill="#fff"/><path d="M7.5 9l5.5 4.5 5.5-4.5" fill="none" stroke="var(--icon)" stroke-width="1"/></svg>COrtega@lanternmgroup.example</li>
    </ul>
  </section>

</main>
</body>
</html>
```